Business cards for KORU Real Estate Holdings LLC

We need a cool, original business card design for a company based in the Washington DC metropolitan area. We are a new energetic and passionate Real Estate Investing Company that invests in all types of real estate; commercial, residential, industrial etc.

Our company color is Red since it reflects action, energy and speed; it is assertive confident, energizing, exciting, powerful, passionate and determined. So we would like business card communicate those qualities to the audience.

Our audiences are investors that want to invest with us, real estate sellers, buyers, and tenants who lease from us.

Our logo is attached

```html
<!DOCTYPE html>
<html lang="en">
<head>
<meta charset="utf-8">
<title>KORU Real Estate Holdings LLC — Business Cards</title>
<link href="https://fonts.googleapis.com/css2?family=Open+Sans:wght@400;600;700;800&display=swap" rel="stylesheet">
<style>
  :root {
    --page-bg: #d3d3d3;
    --card-dark: #2b2727;
    --card-light: #ffffff;
    --brand-red: #c4161c;
    --ink: #2d2d2d;
    --ink-soft: #4a4a4a;
    --stripe-grey: #8f8f8f;
    --stripe-light: #c9c9c9;
    --stripe-black: #111111;
    --deco-peach: #f6e1d9;
  }
  * { box-sizing: border-box; margin: 0; padding: 0; }
  html, body { width: 883px; height: 1200px; overflow: hidden; }
  body {
    background: var(--page-bg);
    font-family: "Open Sans", Arial, sans-serif;
    position: relative;
  }
  .card {
    position: absolute;
    left: 268px;
    width: 390px;
    height: 218px;
    overflow: hidden;
    box-shadow: 0 2px 6px rgba(0,0,0,.18);
  }

  /* Back of card */
  .card--back { top: 373px; background: var(--card-dark); }
  .card--back .frame {
    position: absolute; left: 18px; top: 17px; width: 354px; height: 184px;
    border: 1px solid var(--brand-red);
  }
  .card--back .brand-mark {
    position: absolute; left: 96px; top: 86px; width: 16px; height: 16px;
    border-radius: 50%; background: var(--brand-red);
  }
  .card--back .brand-name {
    position: absolute; left: 120px; top: 70px;
    font-size: 38px; font-weight: 800; letter-spacing: 1px; line-height: 1;
    color: #ffffff;
  }
  .card--back .brand-sub {
    position: absolute; left: 121px; top: 116px;
    font-size: 11px; font-weight: 600; color: #ffffff; letter-spacing: .2px;
  }
  .card--back .web {
    position: absolute; right: 23px; bottom: 19px;
    font-size: 10px; color: var(--brand-red);
  }

  /* Front of card */
  .card--front { top: 608px; background: var(--card-light); }
  .deco { position: absolute; border: 6px solid var(--deco-peach); }
  .deco--a { left: 300px; top: 46px; width: 26px; height: 26px; }
  .deco--b { left: 322px; top: 68px; width: 30px; height: 30px; }
  .deco--c { left: 232px; top: 150px; width: 48px; height: 68px; }
  .card--front .brand-mark {
    position: absolute; left: 22px; top: 60px; width: 16px; height: 16px;
    background: var(--brand-red);
  }
  .card--front .brand-name {
    position: absolute; left: 44px; top: 52px;
    font-size: 30px; font-weight: 800; letter-spacing: 1px; line-height: 1;
    color: var(--ink);
  }
  .card--front .brand-sub {
    position: absolute; left: 40px; top: 84px;
    font-size: 10px; font-weight: 600; color: var(--ink);
  }
  .identity { position: absolute; right: 23px; top: 98px; text-align: right; }
  .identity .name { font-size: 14px; color: var(--brand-red); line-height: 1.1; }
  .identity .role { font-size: 10px; color: var(--ink-soft); line-height: 1.2; }
  .stripes { position: absolute; left: 20px; top: 131px; display: flex; gap: 4px; }
  .stripes span { height: 4px; display: block; }
  .stripes .s1 { width: 140px; background: var(--brand-red); }
  .stripes .s2 { width: 70px; background: var(--stripe-grey); }
  .stripes .s3 { width: 58px; background: var(--stripe-light); }
  .stripes .s4 { width: 68px; background: var(--stripe-black); }
  .contacts { position: absolute; left: 22px; top: 148px; list-style: none; }
  .contacts li {
    display: flex; align-items: center; gap: 7px;
    font-size: 11px; line-height: 13px; color: var(--ink);
  }
  .contacts svg { width: 9px; height: 9px; fill: var(--brand-red); }
  .address {
    position: absolute; right: 23px; top: 148px;
    display: flex; align-items: flex-start; gap: 6px;
  }
  .address p { text-align: right; font-size: 10.5px; line-height: 14px; color: var(--brand-red); }
  .address svg { width: 8px; height: 10px; fill: var(--ink); margin-top: 2px; }
</style>
</head>
<body>
  <section class="card card--back" aria-label="Business card back">
    <div class="frame"></div>
    <span class="brand-mark"></span>
    <div class="brand-name">KORU</div>
    <div class="brand-sub">REAL ESTATE HOLDINGS LLC</div>
    <div class="web">www.yourwebdite.com</div>
  </section>

  <section class="card card--front" aria-label="Business card front">
    <span class="deco deco--a"></span>
    <span class="deco deco--b"></span>
    <span class="deco deco--c"></span>
    <span class="brand-mark"></span>
    <div class="brand-name">KORU</div>
    <div class="brand-sub">REAL ESTATE HOLDINGS LLC</div>

    <div class="identity">
      <div class="name">your name</div>
      <div class="role">designation</div>
    </div>

    <div class="stripes"><span class="s1"></span><span class="s2"></span><span class="s3"></span><span class="s4"></span></div>

    <ul class="contacts">
      <li><svg viewBox="0 0 10 10"><rect x="0" y="3" width="10" height="7" rx="1"/><rect x="1" y="0" width="8" height="3" rx="1"/></svg>0123 456 789</li>
      <li><svg viewBox="0 0 10 10"><path d="M2 0h6v10H2zM3 1v7h4V1z"/></svg>0123 456 789</li>
      <li><svg viewBox="0 0 10 10"><path d="M0 2h10v7H0zM1 3l4 3 4-3z" fill-rule="evenodd"/></svg>youremail@mail.com</li>
      <li><svg viewBox="0 0 10 10"><circle cx="5" cy="5" r="5"/></svg>www.yourwebsite.com</li>
    </ul>

    <div class="address">
      <p>address (street address<br>suite number, city, state, zip</p>
      <svg viewBox="0 0 8 10"><path d="M4 0a4 4 0 0 1 4 4c0 3-4 6-4 6S0 7 0 4a4 4 0 0 1 4-4zm0 2.5a1.5 1.5 0 1 0 0 3 1.5 1.5 0 0 0 0-3z" fill-rule="evenodd"/></svg>
    </div>
  </section>
</body>
</html>
```